Garage Door Business Truck Wrap

looking to create a wrap for a 2012 varnel tallhorn 3400 XT single cab with service bed. please use creativity, here is the website www.bluefernliftdoorsvc.com.. Also, I will upload documents of branded items, Id like everything to seamlessly flow together

```html
<!DOCTYPE html>
<html lang="en">
<head>
<meta charset="utf-8">
<title>Bluefern Lift – Truck Wrap Layout</title>
<link rel="stylesheet" href="https://fonts.googleapis.com/css2?family=Oswald:wght@500&display=swap">
<style>
  :root {
    --backdrop: #e6d2b4;
    --wrap-white: #ffffff;
    --wrap-black: #0b0b0b;
    --gold: #c9a548;
  }
  * { margin: 0; padding: 0; box-sizing: border-box; }
  html, body {
    width: 1200px;
    height: 985px;
    overflow: hidden;
    background: var(--backdrop);
  }
  .sheet {
    position: relative;
    width: 1200px;
    height: 985px;
  }
  .wrap-side {
    position: absolute;
    left: 40px;
    width: 1120px;
    height: 330px;
    box-shadow: 0 14px 24px rgba(80, 60, 30, 0.18);
  }
  .wrap-side--driver { top: 95px; }
  .wrap-side--passenger { top: 560px; }
  .wrap-side svg { display: block; width: 1120px; height: 330px; }

  .panel-white { fill: var(--wrap-white); }
  .panel-black { fill: var(--wrap-black); }
  .band-gold { fill: var(--gold); }

  .brand-name {
    font-family: "Oswald", sans-serif;
    font-weight: 500;
    font-size: 32px;
    letter-spacing: 4px;
    fill: var(--gold);
  }
  .brand-dot { fill: var(--gold); }
  .web-address {
    font-family: "Oswald", sans-serif;
    font-weight: 500;
    font-size: 26px;
    fill: var(--wrap-black);
  }
  .phone-number {
    font-family: "Oswald", sans-serif;
    font-weight: 500;
    font-size: 38px;
    letter-spacing: 6px;
    fill: var(--gold);
  }
  .hours-ring {
    fill: none;
    stroke: var(--gold);
    stroke-width: 3;
  }
  .hours-label {
    font-family: "Oswald", sans-serif;
    font-weight: 500;
    font-size: 20px;
    fill: var(--gold);
  }
</style>
</head>
<body>
<main class="sheet">

  <!-- Driver side: cab on the left, bed on the right -->
  <section class="wrap-side wrap-side--driver">
    <svg viewBox="0 0 1120 330" xmlns="http://www.w3.org/2000/svg">
      <defs>
        <linearGradient id="laurel-tone-a" x1="0" y1="0" x2="0" y2="1">
          <stop offset="0" stop-color="#c9a548"/>
          <stop offset="1" stop-color="#8f6d25"/>
        </linearGradient>
      </defs>
      <rect class="panel-white" x="0" y="0" width="1120" height="330"/>
      <path class="panel-black" d="M600,0 H1120 V330 H520 Q575,170 600,0 Z"/>
      <rect class="band-gold" x="600" y="0" width="520" height="34"/>

      <g role="img" aria-label="Gold laurel branch sweeping down along the seam between cab and bed">
        <path d="M585,18 Q640,150 500,322 L470,322 Q600,170 560,22 Z" fill="url(#laurel-tone-a)"/>
      </g>

      <g class="brand-lockup">
        <circle class="brand-dot" cx="192" cy="183" r="7"/>
        <text class="brand-name" x="212" y="195">BLUEFERN LIFT</text>
      </g>

      <text class="web-address" x="870" y="27" text-anchor="middle">www.bluefernliftdoorsvc.com</text>
      <text class="phone-number" x="870" y="84" text-anchor="middle">555.204.3178</text>

      <g class="hours-badge" transform="translate(1065,155)">
        <circle class="hours-ring" cx="0" cy="0" r="30"/>
        <text class="hours-label" x="0" y="7" text-anchor="middle">24/7</text>
      </g>
    </svg>
  </section>

  <!-- Passenger side: bed on the left, cab on the right -->
  <section class="wrap-side wrap-side--passenger">
    <svg viewBox="0 0 1120 330" xmlns="http://www.w3.org/2000/svg">
      <defs>
        <linearGradient id="laurel-tone-b" x1="0" y1="0" x2="0" y2="1">
          <stop offset="0" stop-color="#c9a548"/>
          <stop offset="1" stop-color="#8f6d25"/>
        </linearGradient>
      </defs>
      <rect class="panel-white" x="0" y="0" width="1120" height="330"/>
      <path class="panel-black" d="M0,0 H520 Q545,170 600,330 H0 Z"/>
      <rect class="band-gold" x="0" y="0" width="520" height="34"/>

      <g role="img" aria-label="Gold laurel branch sweeping down along the seam between bed and cab">
        <path d="M535,18 Q480,150 620,322 L650,322 Q520,170 560,22 Z" fill="url(#laurel-tone-b)"/>
      </g>

      <text class="web-address" x="260" y="27" text-anchor="middle">www.bluefernliftdoorsvc.com</text>
      <text class="phone-number" x="260" y="84" text-anchor="middle">555.204.3178</text>

      <g class="hours-badge" transform="translate(60,155)">
        <circle class="hours-ring" cx="0" cy="0" r="30"/>
        <text class="hours-label" x="0" y="7" text-anchor="middle">24/7</text>
      </g>

      <g class="brand-lockup">
        <circle class="brand-dot" cx="722" cy="183" r="7"/>
        <text class="brand-name" x="742" y="195">BLUEFERN LIFT</text>
      </g>
    </svg>
  </section>

</main>
</body>
</html>
```